Product label for herbal salves, lotions, soaps and tinctures

We need a very simple, clean and organic looking label that can be used for an ointment jar, a lotion bottle and a dropper bottle.
We have an existing logo (see attached). We like the colors white, olive green, gold and black. It needs to include product name as dominant and logo. It also needs to include an ingredient list, and usage statement. Include weight of product, distributed by, made in the USA, and NQB statement.
Example of what needs to be present:
Logo
Name: Calmwick Balm
Used for: For Muscle Aches, Arthritis, Tendonitis, Headaches
To Use: For muscle aches, arthritis and tendonitis, massage into affected area. For tension headache apply to neck, temples and forehead.
Store in a cool and dry place, away from direct heat and sunlight.
Weight of product: 1.75
DIST. BY: Brookmere Herbal
Made in the USA
This product is not intended to diagnose, treat, cure
or prevent any disease. Not regulated
by the NQB. Please consult your health care practitioner
before using product. Discontinue use if any adverse reaction occurs.
Ingredient list:
Wildcrafted Ingredients:
Ashwagandha Root, Peppermint Leaf, Hops Flowers, St. John’s Wort Herb, Arnica Flowers, Green Tea Leaf, Alfalfa Leaf, Dandelion Root, Burdock Root, Chickweed Herb, Chaparral Leaf, Yarrow Flowers, Boneset Herb, Moringa Leaf, Meadowsweet Herb, Nettle Leaf
Organic Ingredients:
Olive Oil, Aloe Leaf, Sweet Birch Bark, Helichrysum Flowers, Holy Basil Leaf, Borage Herb, Ginger Root, Angelica Root, White Willow Bark, Mustard Seed, Beeswax, Vitamin E, Essential Oils
Dimensions of Jar:
Circumference: 7 in.
Height: 1 in.

```html
<!DOCTYPE html>
<html lang="en">
<head>
<meta charset="utf-8">
<title>Calmwick Balm – Jar Label</title>
<link rel="stylesheet" href="https://fonts.googleapis.com/css2?family=Libre+Baskerville:wght@700&family=Mulish:wght@300;400&family=Tinos:wght@400;700&display=swap">
<style>
  :root {
    --page: #f3f3f3;
    --paper: #ffffff;
    --olive: #6a6f27;
    --olive-dark: #5a5f20;
    --gold: #d2901c;
    --gold-line: #d9a233;
    --ink: #1e1e1e;
    --grey-ink: #3b3b3b;
  }
  * { box-sizing: border-box; margin: 0; padding: 0; }
  html, body {
    width: 1200px; height: 1200px; overflow: hidden;
    background: var(--page);
  }
  .label {
    position: absolute;
    left: 39px; top: 520px;
    width: 1122px; height: 161px;
    background: var(--paper);
    box-shadow: 0 1px 3px rgba(0,0,0,0.06);
    overflow: hidden;
  }
  .dist-band {
    position: absolute; left: 0; top: 0;
    width: 36px; height: 100%;
    background: var(--gold);
    display: flex; justify-content: center; align-items: flex-start;
    padding-top: 13px;
  }
  .dist-band p {
    writing-mode: vertical-rl;
    font-family: "Tinos", serif;
    font-weight: 700;
    font-size: 9.4px;
    line-height: 10.5px;
    color: var(--ink);
  }
  .rule {
    position: absolute; left: 36px; right: 0;
    height: 1.5px; background: var(--gold-line);
  }
  .rule.top { top: 7px; }
  .rule.bottom { top: 151px; }

  .usage {
    position: absolute; left: 42px; top: 20px; width: 268px;
    font-family: "Tinos", serif;
    font-size: 11.8px; line-height: 12.7px;
    color: var(--ink);
    text-align: justify;
  }
  .usage p + p { margin-top: 2px; }
  .lead { color: var(--olive); font-weight: 700; }

  .product-name {
    position: absolute; left: 381px; top: 14px; width: 360px;
    font-family: "Libre Baskerville", serif;
    font-weight: 700;
    font-size: 34px; line-height: 40px;
    letter-spacing: -1.6px;
    color: var(--olive);
    text-align: center;
    white-space: nowrap;
  }
  .brand-name {
    position: absolute; left: 384px; top: 82px; width: 110px;
    font-family: "Libre Baskerville", serif;
    font-weight: 700;
    font-size: 16px; line-height: 19px;
    color: var(--olive);
    text-align: center;
  }
  .divider {
    position: absolute; left: 502px; top: 72px;
    width: 1px; height: 71px; background: var(--ink);
  }
  .uses {
    position: absolute; left: 512px; top: 70px;
    font-family: "Mulish", sans-serif;
    font-weight: 300;
    font-size: 18.5px; line-height: 21px;
    color: var(--grey-ink);
    white-space: nowrap;
  }
  .net-weight {
    position: absolute; left: 512px; top: 124px;
    font-family: "Mulish", sans-serif;
    font-weight: 400;
    font-size: 14px; line-height: 17px;
    color: var(--olive-dark);
  }

  .ingredients {
    position: absolute; left: 798px; top: 20px; width: 309px;
    font-family: "Tinos", serif;
    font-size: 11.8px; line-height: 13.3px;
    color: var(--ink);
    text-align: justify;
  }
</style>
</head>
<body>
  <main class="label">
    <aside class="dist-band">
      <p>DIST. BY: Brookmere Herbal<br>Made in the USA</p>
    </aside>
    <div class="rule top"></div>
    <div class="rule bottom"></div>

    <section class="usage">
      <p><span class="lead">To Use:</span> For muscle aches, arthritis and tendonitis, massage into affected area. For tension headache apply to neck, temples and forehead.</p>
      <p>Store in a cool and dry place, away from direct heat and sunlight.</p>
      <p>This product is not intended to diagnose, treat, cure or prevent any disease. Not regulated by the NQB. Please consult your health care practitioner before using product. Discontinue use if any adverse reaction occurs.</p>
    </section>

    <h1 class="product-name">Calmwick Balm</h1>
    <p class="brand-name">Brookmere Herbal</p>
    <div class="divider"></div>
    <p class="uses">For Muscle Aches, Arthritis,<br>Tendonitis, Headaches</p>
    <p class="net-weight">1.75 OZ</p>

    <section class="ingredients">
      <p><span class="lead">Wildcrafted Ingredients:</span> Ashwagandha Root, Peppermint Leaf, Hops Flowers, St. John’s Wort Herb, Arnica Flowers, Green Tea Leaf, Alfalfa Leaf, Dandelion Root, Burdock Root, Chickweed Herb, Chaparral Leaf, Yarrow Flowers, Boneset Herb, Moringa Leaf, Meadowsweet Herb, Nettle Leaf <span class="lead">Organic Ingredients:</span> Olive Oil, Aloe Leaf, Sweet Birch Bark, Helichrysum Flowers, Holy Basil Leaf, Borage Herb, Ginger Root, Angelica Root, White Willow Bark, Mustard Seed, Beeswax, Vitamin E, Essential Oils</p>
    </section>
  </main>
</body>
</html>
```